Meditation for IVF and infertility

I need a flyer inviting IVF patients to join my Meditation class, I would like to offer free meditation to ivf women and for couples this class is free every Thursday night at 5 pm
2437 west harlow ave suite K Santa Barbara Ca 93142
quillbrook-stillness.com for more details

```html
<!DOCTYPE html>
<html lang="en">
<head>
<meta charset="utf-8">
<title>Free Meditation for IVF Women and Couples</title>
<link href="https://fonts.googleapis.com/css2?family=Poppins:wght@300;400;600;700;800&display=swap" rel="stylesheet">
<style>
  :root {
    --page: #e6e6e6;
    --paper: #ffffff;
    --charcoal: #434343;
    --ink: #666666;
    --ink-dark: #555555;
    --lavender: #b59ccd;
    --ring: #a9a9a9;
    --white: #ffffff;
  }
  * { margin: 0; padding: 0; box-sizing: border-box; }
  html, body { width: 1200px; height: 1200px; overflow: hidden; background: var(--page); }
  body { font-family: "Poppins", sans-serif; position: relative; }

  .flyer {
    position: absolute; left: 141px; top: 6px;
    width: 1148px; height: 1486px;
    transform: scale(0.8); transform-origin: top left;
    background: var(--charcoal); overflow: hidden;
    box-shadow: 0 30px 40px rgba(0,0,0,0.25);
  }
  .flyer-shapes { position: absolute; inset: 0; }

  .brand {
    position: absolute; left: 72px; top: 44px; width: 300px; height: 300px;
    border: 3px solid var(--ink-dark); border-radius: 50%;
    display: flex; align-items: center; justify-content: center; text-align: center;
  }
  .brand-name { font-weight: 600; font-size: 30px; line-height: 1.15; color: var(--ink-dark); }

  .headline { position: absolute; left: 0; width: 440px; text-align: center; color: var(--ink); }
  .headline-free { top: 392px; font-weight: 800; font-size: 132px; line-height: 1; letter-spacing: 1px; }
  .headline-band {
    position: absolute; left: 0; top: 523px; width: 436px; height: 73px;
    background: var(--lavender); color: var(--white);
    font-weight: 700; font-size: 54px; line-height: 73px; text-align: center;
  }
  .headline-ivf { top: 610px; line-height: 1; }
  .headline-ivf .light { font-weight: 300; font-size: 50px; }
  .headline-ivf .bold { font-weight: 800; font-size: 72px; }
  .headline-women { top: 676px; font-weight: 800; font-size: 80px; line-height: 1; }
  .headline-andfor { top: 748px; font-weight: 300; font-size: 52px; line-height: 1; }
  .headline-couples { top: 794px; font-weight: 800; font-size: 80px; line-height: 1; }

  .invite { position: absolute; left: 0; width: 1148px; text-align: center; color: var(--white); }
  .invite-title { left: 174px; width: 800px; top: 938px; font-weight: 700; font-size: 56px; line-height: 1; }
  .invite-date { left: 174px; width: 800px; top: 1000px; font-weight: 300; font-size: 44px; line-height: 1; }

  .schedule {
    position: absolute; left: 41px; top: 1076px; width: 1067px; height: 90px;
    border-radius: 45px; overflow: hidden; display: flex;
    box-shadow: 0 24px 30px rgba(0,0,0,0.35);
  }
  .schedule-label, .schedule-time {
    display: flex; align-items: center; justify-content: center;
    font-weight: 700; font-size: 33px;
  }
  .schedule-label { width: 533px; background: var(--lavender); color: var(--white); }
  .schedule-time { flex: 1; background: var(--paper); color: var(--ink); }

  .location { position: absolute; left: 174px; top: 1220px; display: flex; align-items: center; gap: 55px; }
  .location-icon { width: 96px; height: 96px; flex: none; }
  .location-address { font-weight: 300; font-size: 36px; line-height: 46px; color: var(--white); width: 700px; }

  .divider { position: absolute; left: 41px; top: 1357px; width: 1067px; height: 2px; background: #d8d8d8; }

  .website {
    position: absolute; left: 0; width: 1148px; top: 1384px;
    display: flex; align-items: center; justify-content: center; gap: 24px;
    color: var(--white); font-size: 36px; font-weight: 300;
  }
  .website strong { font-weight: 700; }
  .website-icon { width: 56px; height: 56px; }
</style>
</head>
<body>
  <main class="flyer">
    <svg class="flyer-shapes" width="1148" height="1486" viewBox="0 0 1148 1486">
      <defs>
        <clipPath id="photo-circle"><circle cx="935" cy="398" r="495"/></clipPath>
        <linearGradient id="photo-tones" x1="0" y1="0" x2="1" y2="1">
          <stop offset="0" stop-color="#6b5a48"/>
          <stop offset="0.3" stop-color="#4a4c52"/>
          <stop offset="0.6" stop-color="#2f4a70"/>
          <stop offset="1" stop-color="#232427"/>
        </linearGradient>
      </defs>
      <path class="paper-area" d="M0 0 H1148 V520 C880 760 520 930 0 955 Z" fill="#ffffff"/>
      <path class="paper-edge" d="M0 966 C520 941 880 770 1148 530" fill="none" stroke="#9a9a9a" stroke-width="6"/>
      <circle class="photo-ring" cx="935" cy="398" r="507" fill="none" stroke="#a9a9a9" stroke-width="5"/>
      <g clip-path="url(#photo-circle)">
        <rect x="430" y="-100" width="1000" height="1000" fill="url(#photo-tones)" role="img" aria-label="Photo of a row of people seated cross-legged on mats in a meditation class"/>
      </g>
    </svg>

    <div class="brand"><span class="brand-name">Quillbrook<br>Stillness</span></div>

    <div class="headline headline-free">FREE</div>
    <div class="headline-band">MEDITATION</div>
    <div class="headline headline-ivf"><span class="light">TO </span><span class="bold">IVF</span></div>
    <div class="headline headline-women">WOMEN</div>
    <div class="headline headline-andfor">AND FOR</div>
    <div class="headline headline-couples">COUPLES</div>

    <div class="invite invite-title">JOIN US</div>
    <div class="invite invite-date">RE-OPENING JUNE 2021</div>

    <div class="schedule">
      <div class="schedule-label">THIS CLASS IS FREE EVERY</div>
      <div class="schedule-time">THURSDAY NIGHT AT 5 PM</div>
    </div>

    <div class="location">
      <svg class="location-icon" viewBox="0 0 96 96" aria-hidden="true">
        <circle cx="48" cy="48" r="45" fill="none" stroke="#b59ccd" stroke-width="4"/>
        <path d="M48 22 C37 22 30 30 30 40 C30 53 48 72 48 72 C48 72 66 53 66 40 C66 30 59 22 48 22 Z" fill="#ffffff"/>
        <circle cx="48" cy="40" r="7" fill="#434343"/>
      </svg>
      <p class="location-address">2437 west harlow ave suite K Santa Barbara Ca 93142</p>
    </div>

    <div class="divider"></div>

    <p class="website">For more details visit <strong>quillbrook-stillness.com</strong>
      <svg class="website-icon" viewBox="0 0 56 56" aria-hidden="true">
        <path d="M22 20 L48 32 L37 35 L45 46 L41 49 L33 38 L26 46 Z" fill="#ffffff"/>
        <g stroke="#ffffff" stroke-width="3" stroke-linecap="round">
          <line x1="18" y1="4" x2="18" y2="12"/>
          <line x1="6" y1="16" x2="13" y2="16"/>
          <line x1="8" y1="7" x2="13" y2="11"/>
          <line x1="27" y1="7" x2="23" y2="11"/>
          <line x1="8" y1="26" x2="13" y2="22"/>
        </g>
      </svg>
    </p>
  </main>
</body>
</html>
```